VornaRank.com

We need a new web design for our seo services website at vornarank.com.

Right now we have our homepage, and 2 other pages which we use a html code generator. We need a header and footer and a nice professional looking design to showcase our seo plans.

As for the logo we'll use our company vornaforge.com logo Vorna and change Work to Submit and Technologies to Search Engine Marketing.

We also like to display our textfountain widget and author alert sign up box.

Industry/Entity Type

It Company

Requirements

```html
<!DOCTYPE html>
<html lang="en">
<head>
<meta charset="utf-8">
<title>VornaRank.com – Pricing Tables</title>
<link rel="stylesheet" href="https://fonts.googleapis.com/css2?family=Roboto+Condensed:wght@400;700&family=Arimo:wght@400;700&display=swap">
<style>
:root{
  --ink:#333;
  --topbar:#3a3a3a;
  --green:#1f9a2a;
  --teal:#3aa3b4;
  --teal-dark:#2f95a6;
  --head:#3f3f3f;
  --price:#5c5c5c;
  --feat-bg:#fafafa;
  --feat-line:#ececec;
  --feat-text:#7a7a7a;
  --foot-bg:#e4e4e4;
  --btn:#6d6d6d;
  --page-band:#ececec;
  --footer:#333;
  --footer-low:#2b2b2b;
  --muted:#8f8f8f;
  --brand:#1c3f8f;
}
*{box-sizing:border-box;margin:0;padding:0}
html,body{width:960px;height:1200px;overflow:hidden;background:#fff}
body{font-family:"Arimo",Arial,sans-serif;color:var(--ink);position:relative}

.topbar{position:absolute;left:97px;top:0;width:745px;height:22px;background:var(--topbar);color:#ddd;font-size:8px;display:flex;align-items:center;padding:0 3px}
.social{display:flex;gap:4px;margin-left:6px}
.social span{width:10px;height:9px;background:#555;display:block}
.topbar .right{margin-left:auto;display:flex;align-items:center;gap:6px}
.pill{background:var(--green);color:#fff;padding:3px 6px;display:flex;align-items:center;gap:4px}

.header{position:absolute;left:97px;top:22px;width:745px;height:64px}
.logo{position:absolute;left:3px;top:16px;display:flex;align-items:center;gap:7px}
.logo .mark{width:16px;height:16px;background:var(--brand);border-radius:50%}
.logo .name{font-family:"Roboto Condensed",sans-serif;font-weight:700;font-size:21px;color:var(--brand);line-height:1;display:block}
.logo .tag{font-family:"Roboto Condensed",sans-serif;font-weight:700;font-size:8.5px;color:var(--brand);display:block;margin-top:2px;letter-spacing:.2px}
.nav{position:absolute;right:0;top:20px;display:flex;font-family:"Roboto Condensed",sans-serif;font-weight:700;font-size:9.5px}
.nav a{color:#222;text-decoration:none;padding:0 15px;border-left:1px solid #ddd}
.nav a:last-child{border-right:1px solid #ddd}
.nav a.active{color:var(--teal-dark)}

.pageband{position:absolute;left:97px;top:86px;width:745px;height:39px;background:var(--page-band);display:flex;align-items:center;justify-content:space-between;padding:0 3px}
.pageband h1{font-family:"Roboto Condensed",sans-serif;font-size:15px;color:#666;font-weight:700}
.crumbs{font-size:8px;color:#999}

.section-title{position:absolute;left:100px;font-family:"Roboto Condensed",sans-serif;font-weight:700;font-size:15px;color:#333}
.divider{position:absolute;left:100px;top:514px;width:740px;height:1px;background:#eee}

.pricing{position:absolute;left:100px;width:736px;display:flex;align-items:flex-start}
.plan{flex:1;text-align:center;background:var(--feat-bg)}
.plan .name{background:var(--head);color:#fff;font-family:"Roboto Condensed",sans-serif;font-weight:700;font-size:12px;height:28px;line-height:30px;border-top:3px solid #2d2d2d}
.plan .price{background:var(--price);color:#fff;height:64px;padding-top:8px}
.plan .amount{font-family:"Roboto Condensed",sans-serif;font-size:28px;line-height:32px}
.plan .per{font-family:"Roboto Condensed",sans-serif;font-size:8.5px;font-weight:700;margin-top:2px}
.plan ul{list-style:none;padding:8px 10px 10px}
.plan li{font-size:8.5px;color:var(--feat-text);height:17.7px;line-height:17.7px;border-bottom:1px solid var(--feat-line);letter-spacing:.2px}
.plan li:last-child{border-bottom:0}
.plan .foot{background:var(--foot-bg);height:40px;display:flex;align-items:center;justify-content:center}
.btn{font-family:"Roboto Condensed",sans-serif;font-weight:700;font-size:8px;color:#fff;background:var(--btn);border:1px solid #555;border-radius:2px;padding:5px 11px;letter-spacing:-.2px}
.plan.featured{flex:1.12;margin-top:-6px;box-shadow:0 2px 8px rgba(0,0,0,.18);position:relative;z-index:2}
.plan.featured .name{background:var(--teal-dark);border-top:0;height:36px;line-height:36px}
.plan.featured .price{background:var(--teal);height:68px;padding-top:10px}
.plan.featured .foot{height:48px;background:#efefef}
.plan.featured .btn{background:var(--teal);border-color:#2a8898}
.three .plan .name{height:30px;line-height:32px}
.three .plan .price{height:66px}
.three .plan.featured{flex:1}

.footer{position:absolute;left:97px;top:905px;width:745px;height:295px;background:var(--footer);color:#ccc}
.fcol{position:absolute;top:0;height:200px;padding-top:22px}
.fcol h3{font-family:"Roboto Condensed",sans-serif;font-weight:700;font-size:12.5px;color:#fff;margin-bottom:10px}
.links{list-style:none}
.links li{font-size:8.5px;color:var(--muted);height:15.5px}
.links li::before{content:"›";margin-right:5px;color:#aaa}
.blog{display:flex;gap:12px;margin-bottom:8px}
.thumb{width:40px;height:38px;border:2px solid #555;flex:none}
.blog .t{font-size:8.5px;color:var(--muted);line-height:11px}
.blog .d{font-size:7px;color:#5f5f5f;line-height:9px}
.transfer p{font-size:8.5px;color:var(--muted);line-height:12.5px;margin-bottom:12px}
.help{background:var(--green);width:169px;height:72px;position:relative;margin-top:2px}
.help .av{position:absolute;left:15px;top:10px;width:32px;height:28px;background:linear-gradient(#e9d3c2,#b99a86)}
.help p{position:absolute;left:67px;top:12px;width:96px;font-size:7.5px;color:#fff;line-height:10.5px}
.help .tf{position:absolute;left:15px;top:49px;font-size:9px;color:#fff;font-weight:700;font-family:"Roboto Condensed",sans-serif}
.help .tf b{font-size:13px}
.chat{background:var(--green);width:169px;height:50px;margin-top:12px;position:relative}
.chat svg{position:absolute;left:12px;top:10px}
.chat .big{position:absolute;left:71px;top:8px;font-family:"Roboto Condensed",sans-serif;font-size:18px;color:#7be07f}
.chat .small{position:absolute;left:71px;top:30px;font-family:"Roboto Condensed",sans-serif;font-weight:700;font-size:9px;color:#fff}
.fsep{position:absolute;top:0;width:1px;height:200px;background:#3d3d3d}

.lower{position:absolute;left:0;top:200px;width:745px;height:95px;background:var(--footer-low)}
.news{position:absolute;left:3px;top:16px;display:flex;align-items:center}
.news .label{font-family:"Roboto Condensed",sans-serif;font-size:10.5px;color:#fff;line-height:11px;margin-left:12px;width:75px}
.news .field{width:177px;height:20px;background:#252525;border:1px solid #3a3a3a;font-size:7px;color:#666;line-height:18px;padding-left:8px}
.news .sub{background:var(--green);color:#fff;font-family:"Roboto Condensed",sans-serif;font-weight:700;font-size:8.5px;height:20px;line-height:20px;padding:0 10px;margin-left:5px}
.pay{position:absolute;left:384px;top:16px;display:flex;align-items:center;gap:9px}
.pay .label{font-family:"Roboto Condensed",sans-serif;font-size:10.5px;color:#fff;line-height:11px;width:58px}
.pay span{width:40px;height:19px;background:#9a9a9a;border:1px solid #bbb;display:block}
.copy{position:absolute;left:3px;bottom:15px;right:3px;display:flex;justify-content:space-between;font-size:7.5px;color:#4f4f4f}
</style>
</head>
<body>

<div class="topbar">
  <span>Connect With Us:</span>
  <div class="social"><span></span><span></span><span></span><span></span><span></span><span></span><span></span></div>
  <div class="right">
    <span>Call Us:</span>
    <span class="pill"><svg width="9" height="7" viewBox="0 0 9 7"><path d="M1 2 Q4.5 -1 8 2 L7 3 L6 2 L3 2 L2 3 Z M2 4 H7 V7 H2 Z" fill="#fff"/></svg>(088) 555 014 2290</span>
    <span class="pill"><svg width="9" height="7" viewBox="0 0 9 7"><rect width="9" height="7" fill="#fff"/><path d="M0 0 L4.5 4 L9 0" stroke="#1f9a2a" fill="none"/></svg>info@keldhost.com</span>
    <span>Login |</span><span>Help |</span>
    <span class="pill"><svg width="9" height="8" viewBox="0 0 9 8"><ellipse cx="4.5" cy="3.5" rx="4.5" ry="3.3" fill="#fff"/><path d="M2 6 L1 8 L4 6.5Z" fill="#fff"/></svg>Live Chat</span>
  </div>
</div>

<header class="header">
  <div class="logo">
    <span class="mark"></span>
    <div><span class="name">VornaSubmit</span><span class="tag">Search Engine Marketing</span></div>
  </div>
  <nav class="nav">
    <a>HOME</a><a>WEB HOSTING</a><a class="active">FEATURES</a><a>SERVICES</a><a>BLOG</a><a>SUPPORT</a><a>CONTACT</a>
  </nav>
</header>

<div class="pageband"><h1>PRICING TABLES</h1><span class="crumbs">Home / Features / Pricing Tables</span></div>

<h2 class="section-title" style="top:146px">EXAMPLE WITH 4 COLUMNS</h2>

<div class="pricing" style="top:193px">
  <div class="plan">
    <div class="name">ECONOMY</div>
    <div class="price"><div class="amount">$3.99</div><div class="per">/ PER MONTH</div></div>
    <ul><li>Unlimited Bandwidth</li><li>100 GB Space</li><li>10 Databases</li><li>Free Ad Credits</li><li>One Free Domain</li><li>24/7 Unlimited Support</li><li>100 Email Addresses</li></ul>
    <div class="foot"><span class="btn">ORDER NOW</span></div>
  </div>
  <div class="plan featured">
    <div class="name">STANDARD</div>
    <div class="price"><div class="amount">$9.99</div><div class="per">/ PER MONTH</div></div>
    <ul><li>Unlimited Bandwidth</li><li>Unlimited Space</li><li>100 Databases</li><li>Free Ad Credits</li><li>2 Free Domains</li><li>24/7 Unlimited Support</li><li>1000 Email Addresses</li></ul>
    <div class="foot"><span class="btn">ORDER NOW</span></div>
  </div>
  <div class="plan">
    <div class="name">PROFESSIONAL</div>
    <div class="price"><div class="amount">$18.99</div><div class="per">/ PER MONTH</div></div>
    <ul><li>Unlimited Bandwidth</li><li>Unlimited Space</li><li>1000 Databases</li><li>Free Ad Credits</li><li>5 Free Domain</li><li>24/7 Unlimited Support</li><li>Unlimited &nbsp; Emails</li></ul>
    <div class="foot"><span class="btn">ORDER NOW</span></div>
  </div>
  <div class="plan">
    <div class="name">ULTIMATE</div>
    <div class="price"><div class="amount">$60.99</div><div class="per">/ PER MONTH</div></div>
    <ul><li>Unlimited Bandwidth</li><li>Unlimited Space</li><li>Unlimited Databases</li><li>Free Ad Credits</li><li>10 Free Domain</li><li>24/7 Unlimited Support</li><li>Unlimited Emails</li></ul>
    <div class="foot"><span class="btn">ORDER NOW</span></div>
  </div>
</div>

<div class="divider"></div>

<h2 class="section-title" style="top:529px">EXAMPLE WITH 3 COLUMNS</h2>

<div class="pricing three" style="top:577px">
  <div class="plan">
    <div class="name">ECONOMY</div>
    <div class="price"><div class="amount">$3.99</div><div class="per">/ PER MONTH</div></div>
    <ul><li>Unlimited Bandwidth</li><li>100 GB Space</li><li>10 Databases</li><li>Ad Credits</li><li>1 Free Domain</li><li>24/7 Unlimited Support</li><li>100 Email Addresses</li></ul>
    <div class="foot"><span class="btn">ORDER NOW</span></div>
  </div>
  <div class="plan featured">
    <div class="name">STANDARD</div>
    <div class="price"><div class="amount">$9.99</div><div class="per">/ PER MONTH</div></div>
    <ul><li>Unlimited Bandwidth</li><li>Unlimit Space</li><li>100 Database</li><li>Ad Credits</li><li>2 Free Domains</li><li>24/7 Unlimited Support</li><li>1000 Email Addresses</li></ul>
    <div class="foot"><span class="btn">ORDER NOW</span></div>
  </div>
  <div class="plan">
    <div class="name">PROFESSIONAL</div>
    <div class="price"><div class="amount">$18.99</div><div class="per">/ PER MONTH</div></div>
    <ul><li>Unlimited Bandwidth</li><li>Unlimit Space</li><li>1000 Database</li><li>Ad Credits</li><li>5 Free Domain</li><li>24/7 Unlimited Support</li><li>Unlimited &nbsp; Emails</li></ul>
    <div class="foot"><span class="btn">ORDER NOW</span></div>
  </div>
</div>

<footer class="footer">
  <div class="fsep" style="left:168px"></div>
  <div class="fsep" style="left:359px"></div>
  <div class="fsep" style="left:550px"></div>

  <div class="fcol" style="left:3px;width:160px">
    <h3>SUPPORT/HELP</h3>
    <ul class="links"><li>Contact Us</li><li>Knowledge Base</li><li>Downloads</li><li>My Account</li><li>Submit Ticket</li><li>Sign Up</li><li>Affiliates</li><li>Video Tutorials</li><li>Hosting Industry News</li></ul>
  </div>

  <div class="fcol" style="left:193px;width:160px">
    <h3>RECENT BLOG POSTS</h3>
    <div class="blog"><div class="thumb" role="img" aria-label="Blog post photo of pink flowers" style="background:linear-gradient(135deg,#6d8f3a,#c98fb8)"></div><div><div class="t">Lorem Ipsum dummy</div><div class="d">March 01, 2013</div><div class="d">No Comments</div></div></div>
    <div class="blog"><div class="thumb" role="img" aria-label="Blog post photo of a white daisy" style="background:linear-gradient(135deg,#2e5e1c,#d8e6c8)"></div><div><div class="t">There are variations</div><div class="d">March 01, 2013</div><div class="d">No Comments</div></div></div>
    <div class="blog"><div class="thumb" role="img" aria-label="Blog post photo of a butterfly" style="background:linear-gradient(135deg,#4f8a2c,#e39a3b)"></div><div><div class="t">Slightly to believable</div><div class="d">March 01, 2013</div><div class="d">No Comments</div></div></div>
  </div>

  <div class="fcol transfer" style="left:384px;width:165px">
    <h3>TRANSFER YOUR SITE</h3>
    <p>We'll help you t make transferring your website and domain name fast and easy</p>
    <ul class="links"><li>Free Website Transfer</li><li>Free Domain Transfer</li><li>Outstanding reliability</li><li>State-of-the-art Data Center</li><li>Money Back Guarantee</li><li>24/7 Support</li></ul>
  </div>

  <div class="fcol" style="left:574px;width:170px">
    <h3>HAVE ANY QUESTIONS</h3>
    <div class="help">
      <div class="av" role="img" aria-label="Support agent portrait"></div>
      <p>If you have any questions, feel free to call us toll-free</p>
      <div class="tf">Toll-free: <b>1-800-555-0142</b></div>
    </div>
    <div class="chat">
      <svg width="40" height="30" viewBox="0 0 40 30"><ellipse cx="15" cy="11" rx="14" ry="10" fill="#178a21"/><path d="M8 19 L5 27 L15 20Z" fill="#178a21"/><ellipse cx="27" cy="17" rx="12" ry="8" fill="#127a1b"/></svg>
      <div class="big">LIVE CHAT</div>
      <div class="small">WITH OUR AGENTS</div>
    </div>
  </div>

  <div class="lower">
    <div class="news">
      <svg width="20" height="13" viewBox="0 0 20 13"><path d="M1 3 L18 0 L19 10 L2 13Z" fill="#bbb"/><path d="M1 3 L10 8 L18 0" stroke="#777" fill="none"/></svg>
      <div class="label">NEWSLETTER<br>SIGN UP</div>
      <div class="field">Enter your email address</div>
      <div class="sub">SUBSCRIBE</div>
    </div>
    <div class="pay">
      <div class="label">PAYMENTS<br>WE ACCEPT</div>
      <span></span><span></span><span></span><span></span><span></span><span></span>
    </div>
    <div class="copy"><span>Copyright © 2013 VornaRank.com. All rights reserved.</span><span>Terms of Service | Privacy Policy</span></div>
  </div>
</footer>

</body>
</html>
```